Website page design

Hi, I need to improve the look of my homepage and the final offer page of my website. www.Pebble7dock.com We have an orvex buyback program where we purchase used orvex products from consumers nationwide. If you would go click through a sample offer on the site, you will the last view final offer page where we give you a cash offer for you site. I would like to keep the red and white colors since my logo is red and white. Please pay attention to the information shown on the homepage now, it is important for me to show the visitors this information on the home page. I would also love to give the users a friendly and inviting look when clicking on the options of orvex products on the home page.

Target Market(s)

Orvex electronics consumers

Number of Pages Required

2 page

Requirements
Nice to have
• On the final offer page, i would love for the offer to give an exciting look for the pebble 7 dock offer, and a boring look for the orvex buy back offer. At the final offer page you will my websites offer ( Your Pebble7dock Offer ) vs ( Orvex buyback program offer ) which is my competitor.

```html
<!DOCTYPE html>
<html lang="en">
<head>
<meta charset="utf-8">
<title>Pebble7dock – Sell Your Used Orvex Device</title>
<link rel="stylesheet" href="https://fonts.googleapis.com/css2?family=Outfit:wght@400;500;600&family=Arimo:wght@400&display=swap">
<style>
  :root {
    --brand-red: #d11f2e;
    --ink: #111111;
    --body-text: #3a3a3a;
    --page-bg: #fbfafa;
    --white: #ffffff;
    --footer-dark: #38373a;
    --footer-muted: #8e8d92;
    --tile-slate: #652d90;
    --tile-desktop: #14a99c;
    --tile-laptop: #939395;
    --tile-phone: #27a8e0;
  }
  * { box-sizing: border-box; margin: 0; padding: 0; }
  html, body { width: 1200px; height: 2480px; overflow: hidden; }
  body {
    position: relative;
    background: var(--page-bg);
    font-family: "Arimo", Arial, sans-serif;
    color: var(--ink);
  }
  .heading { font-family: "Outfit", Arial, sans-serif; font-weight: 600; }

  /* Header */
  .site-header {
    position: absolute; left: 0; top: 0; width: 1200px; height: 79px;
    background: var(--brand-red);
  }
  .brand { position: absolute; display: flex; align-items: center; gap: 14px; }
  .brand-mark { border: 2px solid var(--white); }
  .brand-name { font-family: "Outfit", Arial, sans-serif; font-weight: 400; color: var(--white); }
  .site-header .brand { left: 108px; top: 23px; }
  .site-header .brand-mark { width: 40px; height: 33px; }
  .site-header .brand-name { font-size: 24px; letter-spacing: 0.5px; }
  .main-nav { position: absolute; right: 63px; top: 19px; display: flex; align-items: center; gap: 20px; }
  .main-nav a { color: var(--white); text-decoration: none; font-family: "Outfit", Arial, sans-serif; font-weight: 500; font-size: 14px; }
  .main-nav .login-btn {
    background: var(--white); color: var(--brand-red); padding: 11px 22px; border-radius: 22px;
  }

  /* Hero */
  .hero { position: absolute; left: 0; top: 79px; width: 1200px; height: 520px; overflow: hidden; }
  .hero-photo {
    position: absolute; inset: 0;
    background:
      radial-gradient(ellipse 260px 150px at 1080px 300px, rgba(170,170,172,0.55), rgba(170,170,172,0) 100%),
      radial-gradient(ellipse 240px 90px at 800px 20px, rgba(120,120,122,0.55), rgba(120,120,122,0) 100%),
      radial-gradient(ellipse 230px 170px at 540px 330px, rgba(246,226,226,0.9), rgba(246,226,226,0) 100%),
      radial-gradient(ellipse 90px 60px at 705px 500px, rgba(150,150,152,0.55), rgba(150,150,152,0) 100%),
      radial-gradient(ellipse 220px 120px at 110px 40px, rgba(200,200,202,0.6), rgba(200,200,202,0) 100%),
      linear-gradient(115deg, #f6f6f6 0%, #f4f3f3 50%, #e1e1e2 72%, #cfcfd0 100%);
  }
  .hero-copy { position: absolute; left: 108px; top: 103px; width: 420px; }
  .hero-title { font-size: 40px; line-height: 48px; }
  .hero-text { margin-top: 18px; font-size: 15px; line-height: 22px; color: var(--body-text); width: 395px; }
  .cta {
    display: inline-block; margin-top: 27px; margin-left: -5px;
    background: var(--brand-red); color: var(--white); text-decoration: none;
    font-family: "Outfit", Arial, sans-serif; font-weight: 500; font-size: 14px;
    padding: 14px 38px; border-radius: 24px;
    box-shadow: 0 10px 18px rgba(90, 100, 200, 0.28);
  }

  /* Partner badges */
  .partners { position: absolute; left: 0; top: 599px; width: 1200px; height: 128px; background: var(--white); }
  .badge { position: absolute; border-radius: 6px; }
  .badge-one { left: 290px; top: 52px; width: 190px; height: 30px; background: #ececec; border-left: 26px solid #2a2a2a; }
  .badge-two { left: 530px; top: 42px; width: 87px; height: 44px; background: #f3e6b8; border-radius: 22px; }
  .badge-three { left: 679px; top: 46px; width: 68px; height: 38px; background: #d4ece2; }
  .badge-four { left: 811px; top: 50px; width: 90px; height: 30px; background: #cfe8d3; border-bottom: 10px solid #2f9e4a; }

  /* Device selection */
  .section-title { position: absolute; left: 0; width: 1200px; text-align: center; font-size: 32px; line-height: 38px; }
  .device-tile { position: absolute; width: 583px; height: 259px; overflow: hidden; }
  .tile-label { position: absolute; top: 50%; transform: translateY(-50%); color: var(--white); font-family: "Outfit", Arial, sans-serif; font-weight: 500; font-size: 23px; z-index: 1; }
  .tile-photo { position: absolute; }
  .tile-slate { left: 12px; top: 916px; background: var(--tile-slate); }
  .tile-desktop { left: 605px; top: 916px; background: var(--tile-desktop); }
  .tile-laptop { left: 12px; top: 1185px; background: var(--tile-laptop); height: 254px; }
  .tile-phone { left: 605px; top: 1185px; background: var(--tile-phone); height: 254px; }

  /* How it works */
  .how-underline { position: absolute; left: 578px; top: 1577px; width: 622px; height: 1px; background: var(--ink); }
  .how-photo {
    position: absolute; left: 700px; top: 1584px; width: 500px; height: 554px;
    background:
      radial-gradient(ellipse 70px 50px at 280px 80px, rgba(40,40,42,0.6), rgba(40,40,42,0) 100%),
      radial-gradient(ellipse 170px 210px at 190px 270px, rgba(165,165,168,0.85), rgba(165,165,168,0) 100%),
      radial-gradient(ellipse 110px 230px at 460px 230px, rgba(214,216,220,0.9), rgba(214,216,220,0) 100%),
      radial-gradient(ellipse 140px 100px at 430px 500px, rgba(236,196,186,0.9), rgba(236,196,186,0) 100%),
      var(--page-bg);
  }
  .step { position: absolute; left: 192px; width: 460px; }
  .step-icon { position: absolute; left: 0; top: 6px; width: 72px; height: 72px; }
  .step-title { margin-left: 100px; font-size: 22px; line-height: 28px; }
  .step-text { margin-left: 100px; margin-top: 8px; font-size: 14px; line-height: 25px; color: var(--body-text); width: 340px; }

  /* Footer */
  .site-footer { position: absolute; left: 0; top: 2138px; width: 1200px; height: 342px; background: var(--footer-dark); overflow: hidden; }
  .footer-wedge { position: absolute; left: 0; top: 0; }
  .site-footer .brand { left: 118px; top: 83px; }
  .site-footer .brand-mark { width: 48px; height: 40px; }
  .site-footer .brand-name { font-size: 28px; }
  .footer-col { position: absolute; top: 87px; }
  .footer-col h3 { color: var(--white); font-family: "Outfit", Arial, sans-serif; font-weight: 600; font-size: 15px; margin-bottom: 14px; }
  .footer-col li { list-style: none; color: var(--footer-muted); font-size: 13px; line-height: 25px; }
  .copyright { position: absolute; left: 114px; top: 288px; color: var(--white); font-size: 12px; }
  .social { position: absolute; left: 1002px; top: 288px; display: flex; gap: 18px; }
  .social span { width: 16px; height: 16px; border-radius: 50%; background: var(--white); display: block; }
</style>
</head>
<body>

<header class="site-header">
  <div class="brand"><span class="brand-mark"></span><span class="brand-name">PEBBLE7DOCK</span></div>
  <nav class="main-nav">
    <a href="#">Home</a>
    <a href="#">Sell</a>
    <a href="#">Track</a>
    <a href="#">Join</a>
    <a href="#" class="login-btn">Login Account</a>
  </nav>
</header>

<section class="hero">
  <div class="hero-photo" role="img" aria-label="Top-down photo of used Orvex laptop, tablet, phone and watch on a white surface"></div>
  <div class="hero-copy">
    <h1 class="hero-title heading">Getting rid of a used orvex product? Sell it to us</h1>
    <p class="hero-text">Ei graece omittantur vel. Habeo persius scaevola qui te. Duo eu mucius nostrum. Causae docendi temporibus vel at. Usu ad postea fabellas, qui nostro iracundia ei.</p>
    <a href="#" class="cta">Select Device</a>
  </div>
</section>

<section class="partners" aria-label="Partner ratings">
  <span class="badge badge-one"></span>
  <span class="badge badge-two"></span>
  <span class="badge badge-three"></span>
  <span class="badge badge-four"></span>
</section>

<h2 class="section-title heading" style="top:808px;">Select Your Device to Receive<br>an Instant Quote</h2>

<a class="device-tile tile-slate" href="#">
  <div class="tile-photo" role="img" aria-label="Orvex slate tablet shown from the front and side" style="left:320px;top:20px;width:210px;height:239px;background:radial-gradient(ellipse 105px 130px at 50% 60%, rgba(60,90,180,0.95), rgba(230,110,110,0.5) 60%, rgba(101,45,144,0) 100%);"></div>
  <span class="tile-label" style="left:70px;">Slates</span>
</a>
<a class="device-tile tile-desktop" href="#">
  <div class="tile-photo" role="img" aria-label="Orvex desktop computer with colourful swirl on screen" style="left:60px;top:0;width:290px;height:259px;background:radial-gradient(ellipse 140px 120px at 50% 45%, rgba(240,120,70,0.95), rgba(200,60,120,0.6) 45%, rgba(60,120,210,0.35) 75%, rgba(20,169,156,0) 100%);"></div>
  <span class="tile-label" style="left:398px;">Desktops</span>
</a>
<a class="device-tile tile-laptop" href="#">
  <div class="tile-photo" role="img" aria-label="Open Orvex laptop seen at an angle" style="left:30px;top:0;width:350px;height:254px;background:radial-gradient(ellipse 170px 125px at 50% 50%, rgba(40,40,42,0.85), rgba(110,110,112,0.5) 55%, rgba(147,147,149,0) 100%);"></div>
  <span class="tile-label" style="left:398px;">Laptops</span>
</a>
<a class="device-tile tile-phone" href="#">
  <div class="tile-photo" role="img" aria-label="Three Orvex phones showing their home screens" style="left:235px;top:20px;width:310px;height:234px;background:radial-gradient(ellipse 150px 120px at 50% 60%, rgba(200,30,60,0.95), rgba(60,40,70,0.6) 55%, rgba(39,168,224,0) 100%);"></div>
  <span class="tile-label" style="left:70px;">Phones</span>
</a>

<h2 class="section-title heading" style="top:1538px;">How It Works</h2>
<div class="how-underline"></div>
<div class="how-photo" role="img" aria-label="Top-down photo of an Orvex tablet, phones and watch on a white surface"></div>

<div class="step" style="top:1601px;">
  <svg class="step-icon" viewBox="0 0 72 72" fill="none" stroke="#d11f2e" stroke-width="2">
    <rect x="12" y="6" width="52" height="38" rx="2"/>
    <rect x="2" y="30" width="26" height="32" rx="2"/>
    <rect x="56" y="38" width="12" height="24" rx="2"/>
    <line x1="30" y1="56" x2="50" y2="56"/><line x1="40" y1="44" x2="40" y2="56"/>
    <line x1="30" y1="30" x2="46" y2="14"/><line x1="8" y1="50" x2="16" y2="42"/>
  </svg>
  <h3 class="step-title heading">Get An Offer</h3>
  <p class="step-text">Lorem ipsum dolor sit amet, ea pro brute facer pro-priae nec epicurei senserit pericula cu. Ea graece animal equidem cum.</p>
</div>

<div class="step" style="top:1761px;">
  <svg class="step-icon" viewBox="0 0 72 72" fill="none" stroke="#d11f2e" stroke-width="2">
    <polygon points="6,28 36,18 66,28 36,38"/>
    <polyline points="12,30 12,58 36,68 60,58 60,30"/>
    <line x1="36" y1="38" x2="36" y2="68"/>
    <circle cx="36" cy="12" r="10"/>
    <polyline points="31,12 35,16 42,8"/>
  </svg>
  <h3 class="step-title heading">Ship It Free</h3>
  <p class="step-text">Lorem ipsum dolor sit amet, ea pro brute facer pro-priae nec epicurei senserit pericula cu. Ea graece animal equidem cum.</p>
</div>

<div class="step" style="top:1921px;">
  <svg class="step-icon" viewBox="0 0 72 72" fill="none" stroke="#d11f2e" stroke-width="2">
    <rect x="2" y="48" width="10" height="18"/>
    <path d="M12 52 h14 l10 4 h14 a4 4 0 0 1 0 8 h-20"/>
    <rect x="60" y="8" width="10" height="18"/>
    <path d="M60 12 h-14 l-10 -4 h-14 a4 4 0 0 0 0 8 h14"/>
    <circle cx="34" cy="30" r="7"/>
  </svg>
  <h3 class="step-title heading">Get Paid Fast</h3>
  <p class="step-text">Lorem ipsum dolor sit amet, ea pro brute facer pro-priae nec epicurei senserit pericula cu. Ea graece animal equidem cum.</p>
</div>

<footer class="site-footer">
  <svg class="footer-wedge" width="1200" height="342" viewBox="0 0 1200 342"><polygon points="0,0 402,0 561,342 0,342" fill="#d11f2e"/></svg>
  <div class="brand"><span class="brand-mark"></span><span class="brand-name">PEBBLE7DOCK</span></div>
  <div class="footer-col" style="left:661px;">
    <h3>Get In Touch</h3>
    <ul><li>Pebble7dock</li><li>48 Larkspur Lane</li><li>Millbrook Falls, NY, 10990</li><li>555-014-2271</li></ul>
  </div>
  <div class="footer-col" style="left:856px;">
    <h3>Support</h3>
    <ul><li>Sell</li><li>Track</li><li>About Us</li><li>FAQs</li><li>Contact Us</li></ul>
  </div>
  <div class="footer-col" style="left:986px;">
    <h3>Legal</h3>
    <ul><li>Terms of Service</li><li>Privacy Policy</li><li>Contact Us</li></ul>
  </div>
  <p class="copyright">© 2019 – All rights reserved.</p>
  <div class="social" aria-label="Social links"><span></span><span></span><span></span></div>
</footer>

</body>
</html>
```